I need to redesign this website. Modern Fun Professional Redesign For www.JollyPerkHub.com = New Name www.ClaimVouchly.com

Use existing content as it is on website exactly and we will revise after initial mock ups.

The new name will be ClaimVouchly.com please make a quick logo for this site too while redesigning.

Make it look like an official website....

Target Market(s)

Consumers that are redeeming certificates that businesses gave to them as a gift for customer loyalty,e tc.

Industry/Entity Type

It Professional

Logo Text

www.ClaimVouchly.com

Number of Pages Required

4 page

Colors

Designer to choose colors to be used in the design.

Requirements
Must have
• Must look professional, build trust and credibility.
Nice to have
• open
Should not have
• open

```html
<!DOCTYPE html>
<html lang="en">
<head>
<meta charset="utf-8">
<title>ClaimVouchly – Redemption Processing Center</title>
<link href="https://fonts.googleapis.com/css2?family=Lato:ital,wght@0,400;0,700;1,400&display=swap" rel="stylesheet">
<style>
:root{
  --blue:#0b8fd4;
  --orange:#f58220;
  --green:#4a9a35;
  --ink:#333333;
  --muted:#4a4a4a;
  --grey-bg:#ececec;
  --quote:#6e6e6e;
  --footer:#333333;
  --overlay:rgba(58,58,58,.72);
}
*{margin:0;padding:0;box-sizing:border-box}
html,body{width:1140px;height:1200px;overflow:hidden;background:#fff}
body{font-family:'Lato',sans-serif;color:var(--ink);position:relative}
.site-header{position:absolute;left:0;top:0;width:1140px;height:107px;background:#fff}
.brand{position:absolute;left:76px;top:16px;display:flex;align-items:center;gap:18px}
.brand-mark{width:72px;height:72px;border-radius:50%;background:var(--blue)}
.brand-name{font-size:32px;font-weight:700;color:var(--blue);line-height:1}
.brand-tag{font-size:17px;color:var(--ink);margin-top:8px;letter-spacing:.2px}
.phone{position:absolute;right:79px;top:14px;display:flex;align-items:center;gap:8px;font-size:16px;color:var(--ink)}
.phone-icon{width:30px;height:30px;border-radius:50%;background:var(--green);display:flex;align-items:center;justify-content:center}
.main-nav{position:absolute;right:79px;top:64px;display:flex;font-size:15px}
.main-nav a{color:var(--ink);text-decoration:none;padding:0 25px;border-left:1px solid #ccc;line-height:15px}
.main-nav a:first-child{border-left:none}
.main-nav a:last-child{padding-right:0}
.main-nav a.active{color:var(--blue)}
.hero{position:absolute;left:0;top:107px;width:1140px;height:467px;
  background:linear-gradient(180deg,#8fc6e4 0%,#b8dbee 30%,#c9b79a 50%,#4f8db4 70%,#2d6b98 100%)}
.hero-panel{position:absolute;left:76px;top:98px;width:987px;height:271px;background:var(--overlay);text-align:center;color:#fff}
.hero-panel h1{font-weight:400;font-size:37px;margin-top:30px;letter-spacing:.3px}
.hero-panel p{font-size:20px;text-transform:uppercase;line-height:42px}
.hero-panel p:first-of-type{margin-top:8px}
.redeem-form{position:absolute;left:58px;top:180px;width:872px;height:57px;background:#c9c9c9;padding:5px 7px 5px 7px;display:flex}
.redeem-form .field{flex:1;background:#fff;border:1px solid #bbb}
.redeem-form .go{width:119px;background:var(--green);color:#fff;font-size:30px;display:flex;align-items:center;justify-content:center}
.about{position:absolute;left:0;top:574px;width:1140px;height:161px;text-align:center;font-size:15.2px;color:var(--muted)}
.about p{line-height:23px}
.about p:first-child{margin-top:27px}
.about p + p{margin-top:2px}
.about strong{color:var(--ink)}
.testimonials{position:absolute;left:0;top:735px;width:1140px;height:418px;background:var(--grey-bg)}
.section-title{position:absolute;left:0;width:1140px;top:38px;text-align:center;font-size:29px;font-weight:400;color:var(--blue)}
.section-title span{color:var(--orange)}
.title-rule{position:absolute;left:551px;top:90px;width:39px;height:1px;background:#b9b9b9}
.card{position:absolute;top:117px;width:312px;height:217px;background:#fff;border:1px solid #d6d6d6;overflow:hidden}
.quote-badge{position:absolute;left:18px;top:21px;width:76px;height:76px;border-radius:50%;background:var(--quote);display:flex;align-items:center;justify-content:center}
.reviewer{position:absolute;left:110px;top:36px;font-size:16.5px;color:var(--blue)}
.stars{position:absolute;left:110px;top:65px;display:flex;gap:4px}
.review{position:absolute;left:15px;right:8px;top:108px;font-size:12.7px;line-height:22.8px;color:var(--muted)}
.view-all{position:absolute;left:0;width:1140px;top:357px;text-align:center;font-size:16px;font-style:italic;color:var(--green);text-decoration:underline}
.site-footer{position:absolute;left:0;top:1153px;width:1140px;height:47px;background:var(--footer);color:#fff}
.copyright{position:absolute;left:78px;top:15px;font-size:14.5px}
.social{position:absolute;right:78px;top:8px;display:flex;gap:9px}
.social span{width:30px;height:30px;border-radius:50%}
</style>
</head>
<body>
<header class="site-header">
  <div class="brand">
    <div class="brand-mark"></div>
    <div>
      <div class="brand-name">ClaimVouchly</div>
      <div class="brand-tag">Redemption Processing Center</div>
    </div>
  </div>
  <div class="phone">
    <span class="phone-icon"><svg width="16" height="16" viewBox="0 0 24 24"><path fill="#fff" d="M6.6 10.8c1.4 2.8 3.8 5.1 6.6 6.6l2.2-2.2c.3-.3.7-.4 1-.2 1.1.4 2.3.6 3.6.6.6 0 1 .4 1 1V20c0 .6-.4 1-1 1C10.6 21 3 13.4 3 4c0-.6.4-1 1-1h3.5c.6 0 1 .4 1 1 0 1.3.2 2.5.6 3.6.1.3 0 .7-.2 1z"/></svg></span>
    555-014-2368
  </div>
  <nav class="main-nav">
    <a class="active" href="#">Home</a>
    <a href="#">Testimonials</a>
    <a href="#">Terms</a>
    <a href="#">Contact Us</a>
  </nav>
</header>

<section class="hero" role="img" aria-label="Travel collage of world landmarks, airplanes and birds over a globe under a blue sky">
  <div class="hero-panel">
    <h1>Welcome To ClaimVouchly</h1>
    <p>Please enter a valid certificate ID in the form below</p>
    <p>to redeem your certificate and to view FAQ's, terms and locations.</p>
    <div class="redeem-form">
      <div class="field"></div>
      <div class="go">Go</div>
    </div>
  </div>
</section>

<section class="about">
  <p>ClaimVouchly.com is a leading company in travel certificate fulfillment.</p>
  <p>Our goal is to make it easy for you to redeem your certificate and our philosophy is this:<br><strong>"What good is it to receive a gift certificate if you can't use it?"</strong>.</p>
  <p>If you have any questions about how to redeem a certain certificate, please contact us. We are here to help.</p>
</section>

<section class="testimonials">
  <h2 class="section-title">Client <span>Testimonials</span></h2>
  <div class="title-rule"></div>

  <article class="card" style="left:76px">
    <div class="quote-badge"><svg width="38" height="30" viewBox="0 0 38 30"><g fill="#fff"><circle cx="9" cy="9" r="8"/><path d="M17 9c0 9-5 16-14 19l-1-4c5-2 8-6 8-11z"/><circle cx="29" cy="9" r="8"/><path d="M37 9c0 9-5 16-14 19l-1-4c5-2 8-6 8-11z"/></g></svg></div>
    <div class="reviewer">Lena P.</div>
    <div class="stars"><svg width="84" height="12" viewBox="0 0 84 12"><g fill="#f58220"><polygon id="s" points="6,0 7.8,4 12,4.4 8.8,7.2 9.8,11.6 6,9.3 2.2,11.6 3.2,7.2 0,4.4 4.2,4"/><use href="#s" x="18"/><use href="#s" x="36"/><use href="#s" x="54"/><use href="#s" x="72"/></g></svg></div>
    <p class="review">Ruth was a "saving grace.' She followed up and helped me book the vacation and air fare. Ruth was positive and did everything she promised to do.</p>
  </article>

  <article class="card" style="left:421px">
    <div class="quote-badge"><svg width="38" height="30" viewBox="0 0 38 30"><g fill="#fff"><circle cx="9" cy="9" r="8"/><path d="M17 9c0 9-5 16-14 19l-1-4c5-2 8-6 8-11z"/><circle cx="29" cy="9" r="8"/><path d="M37 9c0 9-5 16-14 19l-1-4c5-2 8-6 8-11z"/></g></svg></div>
    <div class="reviewer" style="left:108px">Owen Hale</div>
    <div class="stars" style="left:108px"><svg width="84" height="12" viewBox="0 0 84 12"><g fill="#f58220"><use href="#s"/><use href="#s" x="18"/><use href="#s" x="36"/><use href="#s" x="54"/><use href="#s" x="72"/></g></svg></div>
    <p class="review" style="left:19px">Jonah was able to put together our flight schedule. He was very patient with us and diligent in working out all the changes I was requesting. Thank you, Jonah.</p>
  </article>

  <article class="card" style="left:751px">
    <div class="quote-badge"><svg width="38" height="30" viewBox="0 0 38 30"><g fill="#fff"><circle cx="9" cy="9" r="8"/><path d="M17 9c0 9-5 16-14 19l-1-4c5-2 8-6 8-11z"/><circle cx="29" cy="9" r="8"/><path d="M37 9c0 9-5 16-14 19l-1-4c5-2 8-6 8-11z"/></g></svg></div>
    <div class="reviewer">Curtis Nolan</div>
    <div class="stars"><svg width="84" height="12" viewBox="0 0 84 12"><g fill="#f58220"><use href="#s"/><use href="#s" x="18"/><use href="#s" x="36"/><use href="#s" x="54"/><use href="#s" x="72"/></g></svg></div>
    <p class="review" style="left:21px;right:6px;letter-spacing:-.1px">Our vacation was great!!!! We stayed at the Marlowe Grand. And we had a lot of fun. We do not have any pictures as everyone else took them. We celebrated our grandson's 21st birthday.</p>
  </article>

  <div class="view-all">View All +</div>
</section>

<footer class="site-footer">
  <div class="copyright">Copyright © 2017 ClaimVouchly. All Rights Reserved.</div>
  <div class="social" aria-label="Social links">
    <span style="background:#1d5fb0"></span>
    <span style="background:#13c1d6"></span>
    <span style="background:#0c8fd0"></span>
    <span style="background:#ef3e26"></span>
  </div>
</footer>
</body>
</html>
```